Letterbox promotional card

Boutique real estate agency needs postcard (no address/stamp space) to promote business via letterboxing, café distribution, etc.
Needs contact details as per attached business card, clean look, company colours, logo and catch phrase as per the T-shirt design attached.
Do not include 'Sales' from the business card. Add another name and mobile number-
Velko Marrandine 0438 917 264

Target Market(s)

Potential property vendors.

Industry/Entity Type

Real Estate

Requirements
Must have
• REVISEDText for reverse side of card: Use dot points, one per line - (no dot point for the Considering selling?)-
• Considering selling?
• No obligation appraisal
• Integrity
• Personalised service
• Individualised marketing programs
• Quality
Nice to have
• Considering selling?
• No obligation appraisal
• Integrity
• Personalised service
Should not have
• Property photos; too much text

```html
<!DOCTYPE html>
<html lang="en">
<head>
<meta charset="utf-8">
<title>Harwell Brook Real Estate – Letterbox Card</title>
<link href="https://fonts.googleapis.com/css2?family=Raleway:wght@400;500;600;800&display=swap" rel="stylesheet">
<style>
  :root {
    --navy: #1f3a52;
    --gold: #b8962e;
    --ink: #1d2a36;
    --paper: #ffffff;
    --backdrop: #e4e6e8;
    --photo-top: #9a9088;
    --photo-bottom: #5e5650;
  }
  * { box-sizing: border-box; margin: 0; padding: 0; }
  html, body { width: 900px; height: 1200px; overflow: hidden; }
  body {
    background: var(--backdrop);
    font-family: "Raleway", sans-serif;
    color: var(--ink);
    position: relative;
  }
  .card {
    position: absolute;
    left: 60px;
    width: 780px;
    height: 400px;
    background: var(--paper);
    box-shadow: 0 6px 18px rgba(0,0,0,0.18);
    overflow: hidden;
  }
  .card--front { top: 130px; }
  .card--back { top: 670px; }

  /* Front */
  .brand {
    position: absolute;
    top: 88px; left: 0; right: 0;
    text-align: center;
  }
  .brand__name {
    font-weight: 800;
    font-size: 44px;
    line-height: 1.05;
    letter-spacing: 2px;
    text-transform: uppercase;
    color: var(--navy);
  }
  .brand__tagline {
    margin-top: 22px;
    font-weight: 400;
    font-size: 31px;
    color: var(--gold);
  }
  .brand__web {
    margin-top: 10px;
    font-weight: 500;
    font-size: 22px;
    letter-spacing: 0.5px;
    color: var(--ink);
  }
  .front-band {
    position: absolute;
    left: 0; bottom: 0;
    width: 100%; height: 34px;
  }

  /* Back */
  .team {
    position: absolute;
    left: 36px; top: 26px;
    width: 150px;
  }
  .member { text-align: center; margin-bottom: 14px; }
  .member__photo {
    width: 150px; height: 112px;
    background: linear-gradient(160deg, var(--photo-top), var(--photo-bottom));
  }
  .member__name {
    margin-top: 4px;
    font-size: 13px;
    font-weight: 600;
    color: var(--gold);
  }
  .member__phone { font-size: 13px; font-weight: 500; }

  .pitch {
    position: absolute;
    left: 232px; top: 28px;
    width: 500px;
  }
  .pitch__heading {
    font-size: 30px;
    font-weight: 600;
    color: var(--gold);
  }
  .pitch__list {
    list-style: none;
    margin-top: 6px;
  }
  .pitch__list li {
    font-size: 18px;
    font-weight: 500;
    line-height: 1.3;
    color: var(--navy);
  }
  .pitch__list li::before {
    content: "•";
    color: var(--gold);
    margin-right: 8px;
  }
  .pitch__rule {
    margin: 20px 0 0 0;
    width: 330px;
    height: 2px;
    background: var(--gold);
  }
  .contact {
    position: absolute;
    left: 270px; top: 262px;
    font-size: 16px;
    line-height: 1.3;
    font-weight: 500;
  }
  .contact__label { color: var(--gold); font-weight: 600; }

  .footer-band {
    position: absolute;
    left: 0; bottom: 0;
    width: 100%; height: 30px;
    background: var(--navy);
    color: var(--gold);
    font-size: 12px;
    text-align: center;
    line-height: 30px;
    letter-spacing: 0.3px;
  }
</style>
</head>
<body>

<section class="card card--front">
  <div class="brand">
    <div class="brand__name">Harwell Brook<br>Real Estate</div>
    <div class="brand__tagline">Making a difference</div>
    <div class="brand__web">www.harwellbrook.com</div>
  </div>
  <svg class="front-band" viewBox="0 0 780 34" preserveAspectRatio="none">
    <polygon points="0,10 780,0 780,6 0,16" fill="var(--gold)"/>
    <polygon points="0,16 780,6 780,34 0,34" fill="var(--navy)"/>
  </svg>
</section>

<section class="card card--back">
  <div class="team">
    <div class="member">
      <div class="member__photo" role="img" aria-label="Portrait photo of Velko Marrandine"></div>
      <div class="member__name">Velko Marrandine</div>
      <div class="member__phone">0438 917 264</div>
    </div>
    <div class="member">
      <div class="member__photo" role="img" aria-label="Portrait photo of Maren Tolliver with her dog"></div>
      <div class="member__name">Maren Tolliver</div>
      <div class="member__phone">0427 381 590</div>
    </div>
  </div>

  <div class="pitch">
    <h2 class="pitch__heading">Considering selling?</h2>
    <ul class="pitch__list">
      <li>No obligation appraisal</li>
      <li>Integrity</li>
      <li>Quality</li>
      <li>Personalised service</li>
      <li>Individualised marketing programs</li>
    </ul>
    <div class="pitch__rule"></div>
  </div>

  <address class="contact" style="font-style: normal;">
    <div>142 Kendall St, Millbrook NSW 2591</div>
    <div><span class="contact__label">Phone</span> 02 4907 3185</div>
    <div><span class="contact__label">Fax</span> 02 4907 3190</div>
    <div><span class="contact__label">Mobile</span> 0427 381 590</div>
    <div><span class="contact__label">Email</span> velko@harwellbrook.com</div>
  </address>

  <div class="footer-band">Real Estate and Stock and Station Agent Licence Number 2048815 ABN 31 604 258 117</div>
</section>

</body>
</html>
```